Stationary for New Company

We need stationary designed for a new company. Details of the required stationary is attached.

The final version should be trendy, clean... only 2 colours (green + grey/black) and professional.

#1: Business Cards (design on 2 sides)
#2: Letterhead (word format)
#3: Cover Page and back cover for proposals
#4: Envelopes,
#5: Thank You card,
#6: Presentation Folder,
#7: Email signatures template (sample attached in word document)

Logo is attached. Logo can be reversed out (will attach once available). Logo can be stacked or horizontal (provided as horizontal).

Files need to be provided in ai + png format.

Target Market(s)

Business owners. More affluent.

Industry/Entity Type

Business

Requirements
Must have
• See brief

Font: Calibri
Should not have
• Photographs / stock photos

```html
<!DOCTYPE html>
<html lang="en">
<head>
<meta charset="utf-8">
<title>Parkline Insurance Brokers – Presentation Folder</title>
<link rel="stylesheet" href="https://fonts.googleapis.com/css2?family=Open+Sans:wght@400;600;700&display=swap">
<style>
  :root {
    --green: #6f9a2a;
    --green-dark: #5d8421;
    --green-light: #86ad3c;
    --white: #ffffff;
    --stage: #e4e4e4;
    --stage-edge: #c9c9c9;
    --sky-top: #8fb6de;
    --sky-low: #d6e6f3;
    --grass: #7fa64a;
    --font: "Open Sans", Calibri, Arial, sans-serif;
  }
  * { box-sizing: border-box; margin: 0; padding: 0; }
  html, body { width: 1200px; height: 847px; overflow: hidden; }
  body {
    background: radial-gradient(ellipse at 55% 30%, #f7f7f7 0%, var(--stage) 55%, var(--stage-edge) 100%);
    font-family: var(--font);
    position: relative;
  }
  .folder {
    position: absolute;
    left: 190px; top: 150px;
    width: 820px; height: 548px;
    display: flex;
    box-shadow: 0 18px 40px rgba(0,0,0,0.28);
  }
  .panel { position: relative; width: 410px; height: 548px; overflow: hidden; }

  /* Back cover */
  .back-cover { background: linear-gradient(160deg, var(--green-light) 0%, var(--green) 55%, var(--green-dark) 100%); }
  .back-contact {
    position: absolute; left: 30px; bottom: 40px;
    color: var(--white); font-size: 8.5px; letter-spacing: 1.2px; line-height: 1.45;
  }
  .back-contact .group { margin-bottom: 9px; }
  .back-contact b { font-weight: 700; }

  /* Front cover */
  .front-cover { background: var(--green); }
  .cover-photo {
    position: absolute; left: 0; top: 0; width: 410px; height: 205px;
    background:
      linear-gradient(90deg, var(--white) 0%, rgba(255,255,255,0) 30%),
      linear-gradient(180deg, var(--sky-top) 0%, var(--sky-low) 72%, var(--grass) 82%, var(--green-dark) 100%);
  }
  .client-tag {
    position: absolute; right: 14px; top: 14px;
    background: var(--white); color: var(--green);
    font-size: 10px; letter-spacing: 1.6px;
    padding: 5px 22px 5px 26px; border-radius: 14px 0 0 14px;
  }
  .brand-band {
    position: absolute; left: 0; top: 205px; width: 410px; height: 68px;
    background: var(--white);
    display: flex; align-items: center; justify-content: space-between;
    padding: 0 18px 0 20px;
  }
  .brand { display: flex; align-items: center; gap: 7px; }
  .brand-square { width: 26px; height: 26px; background: var(--green); }
  .brand-name { color: var(--green); font-size: 19px; font-weight: 400; line-height: 1; }
  .brand-name small { display: block; font-size: 8.5px; margin-top: 2px; }
  .cover-title { text-align: right; color: var(--green); font-weight: 700; }
  .cover-title .label { font-size: 9px; letter-spacing: 0.3px; }
  .cover-title .years { font-size: 21px; line-height: 1.05; }

  .contacts {
    position: absolute; left: 22px; top: 290px; display: flex; gap: 36px;
    color: var(--white);
  }
  .contact-card .name { font-size: 9.5px; font-weight: 700; letter-spacing: 1px; }
  .contact-card .role { font-size: 8px; letter-spacing: 0.8px; margin-bottom: 9px; }
  .contact-card .addr { font-size: 6px; letter-spacing: 0.8px; line-height: 1.5; margin-bottom: 8px; }
  .contact-card ul { list-style: none; font-size: 6px; letter-spacing: 0.8px; }
  .contact-card li { display: flex; align-items: center; gap: 7px; margin-bottom: 3px; }
  .contact-card svg { width: 9px; height: 9px; fill: var(--white); }

  .front-footer {
    position: absolute; left: 22px; bottom: 28px;
    color: var(--white); font-size: 8px; letter-spacing: 1.3px; line-height: 1.7;
  }
  .front-footer b { font-weight: 700; }
</style>
</head>
<body>
  <main class="folder">
    <section class="panel back-cover">
      <div class="back-contact">
        <div class="group">5820 41st Avenue NW<br>Riverton, AB T5K 2L8</div>
        <div class="group">
          <b>Phone:</b> 555.210.4400<br>
          <b>Fax:</b> 555.210.4410<br>
          <b>Toll Free:</b> 800.555.0199
        </div>
        <div><b>Website:</b> www.parklineinsurance.com</div>
      </div>
    </section>

    <section class="panel front-cover">
      <div class="cover-photo" role="img" aria-label="Photograph of a family standing on a green field under a blue sky, raising their arms toward sketched house, car and bicycle clouds"></div>
      <div class="client-tag">Vantoria Labs Inc</div>

      <div class="brand-band">
        <div class="brand">
          <span class="brand-square"></span>
          <span class="brand-name">Parkline<small>Insurance Brokers</small></span>
        </div>
        <div class="cover-title">
          <div class="label">INSURANCE PROGRAM PORTOFOLIO</div>
          <div class="years">2014 - 2015</div>
        </div>
      </div>

      <div class="contacts">
        <div class="contact-card">
          <div class="name">Owen Marsh, BA, CRM</div>
          <div class="role">President &amp; CEO</div>
          <div class="addr">5820 41st Avenue NW<br>Riverton, AB T5K 2L8</div>
          <ul>
            <li><svg viewBox="0 0 10 10"><path d="M1 3c0-1 1-2 4-2s4 1 4 2v1H7V3H3v1H1zM2 5h6l1 4H1z"/></svg>555.210.4400</li>
            <li><svg viewBox="0 0 10 10"><path d="M3 1h4v2H3zM1 4h8v4H7v1H3V8H1z"/></svg>555.210.4410</li>
            <li><svg viewBox="0 0 10 10"><path d="M1 3c0-1 1-2 4-2s4 1 4 2v1H7V3H3v1H1zM2 5h6l1 4H1z"/></svg>800.555.0199 (Toll Free)</li>
          </ul>
        </div>
        <div class="contact-card">
          <div class="name">Owen Marsh, BA, CRM</div>
          <div class="role">President &amp; CEO</div>
          <div class="addr">5820 41st Avenue NW<br>Riverton, AB T5K 2L8</div>
          <ul>
            <li><svg viewBox="0 0 10 10"><path d="M1 3c0-1 1-2 4-2s4 1 4 2v1H7V3H3v1H1zM2 5h6l1 4H1z"/></svg>555.210.4400</li>
            <li><svg viewBox="0 0 10 10"><path d="M3 1h4v2H3zM1 4h8v4H7v1H3V8H1z"/></svg>555.210.4410</li>
            <li><svg viewBox="0 0 10 10"><path d="M1 3c0-1 1-2 4-2s4 1 4 2v1H7V3H3v1H1zM2 5h6l1 4H1z"/></svg>800.555.0199 (Toll Free)</li>
          </ul>
        </div>
      </div>

      <div class="front-footer">
        5820 41st Avenue NW &nbsp;&nbsp; Riverton, AB T5K 2L8<br>
        <b>Phone</b> 555.210.4400 &nbsp; <b>Website</b> &nbsp;www.parklinebrokers.com
      </div>
    </section>
  </main>
</body>
</html>
```